Toravelle Works Luxury Candles

Luxury box design,, simple and sophisticated look,,

My collection of candles come in 5 different fragrances, i would like to be able to change the fragrance name on the boxes,,,,

I would like the outline of australia on the front down the bottom , (only small) to represent this is an australian product.

My boxes are white gloss,,,

Happy for you to use my current logo ,,, however you'll have to change Toravelle Nails to Toravelle Works.

```html
<!DOCTYPE html>
<html lang="en">
<head>
<meta charset="utf-8">
<title>Toravelle Works Luxury Candles – Box Fronts</title>
<link rel="stylesheet" href="https://fonts.googleapis.com/css2?family=Cormorant+Garamond:wght@500&display=swap">
<style>
  :root {
    --page-bg: #eef5f8;
    --box-white: #ffffff;
    --box-edge: #e2e6e9;
    --logo-band: #f1f1f1;
    --ink: #1d1d1d;
    --outline-tone: #d9dcdf;
    --caramel: #a8776a;
    --caramel-low: #4c5666;
    --amber: #d7a524;
    --amber-low: #8b8a1f;
    --lime: #7d9a3c;
    --lime-low: #2f7d3a;
    --cotton: #6f93d6;
    --cotton-low: #1f6fd0;
    --blossom: #e6479a;
    --blossom-low: #c0269a;
  }
  * { box-sizing: border-box; margin: 0; padding: 0; }
  html, body {
    width: 1200px; height: 702px; overflow: hidden;
    background: var(--page-bg);
  }
  .canvas {
    width: 1200px; height: 702px;
    display: flex; justify-content: center; align-items: center; gap: 30px;
  }
  .box-front {
    width: 196px; height: 284px;
    background: var(--box-white);
    border: 1px solid var(--box-edge);
    box-shadow: 0 6px 18px rgba(60, 90, 110, 0.12);
    display: flex; flex-direction: column; align-items: center;
    padding-top: 78px;
  }
  .brand-band {
    width: 140px; height: 24px;
    background: var(--logo-band);
    display: flex; align-items: center; justify-content: center;
    font-family: "Cormorant Garamond", serif;
    font-weight: 500; font-size: 15px; color: var(--ink);
  }
  .foil-panel {
    position: relative;
    width: 136px; height: 150px; margin-top: 12px;
    display: flex; align-items: center; justify-content: center;
  }
  .foil-panel .foil-texture {
    position: absolute; inset: 0;
  }
  .fragrance-name {
    position: relative;
    font-family: "Cormorant Garamond", serif;
    font-weight: 500; font-size: 11px; letter-spacing: 0.02em;
    color: var(--ink); text-transform: uppercase; white-space: nowrap;
  }
  .origin-mark {
    width: 34px; height: 32px; margin-top: 10px;
    background: var(--outline-tone); border-radius: 4px;
  }
  .vanilla-caramel .foil-texture { background: linear-gradient(225deg, var(--caramel) 0%, #e7dcd8 40%, #f4f4f4 60%, var(--caramel-low) 100%); }
  .egyptian-amber .foil-texture { background: linear-gradient(225deg, var(--amber) 0%, #f1e3ae 40%, #f7f5ea 60%, var(--amber-low) 100%); }
  .coconut-lime .foil-texture { background: linear-gradient(225deg, var(--lime) 0%, #dbe5c4 40%, #f4f7ef 60%, var(--lime-low) 100%); }
  .cotton-candy .foil-texture { background: linear-gradient(225deg, var(--cotton) 0%, #d6e1f4 40%, #f3f6fc 60%, var(--cotton-low) 100%); }
  .cherry-blossom .foil-texture { background: linear-gradient(225deg, var(--blossom) 0%, #f6c8e0 40%, #fbf1f6 60%, var(--blossom-low) 100%); }
</style>
</head>
<body>
<main class="canvas">
  <section class="box-front vanilla-caramel">
    <div class="brand-band">Toravelle Works</div>
    <div class="foil-panel">
      <div class="foil-texture" role="img" aria-label="Textured metallic foil in caramel and slate tones"></div>
      <span class="fragrance-name">Vanilla Caramel</span>
    </div>
    <div class="origin-mark" role="img" aria-label="Small outline of Australia"></div>
  </section>
  <section class="box-front egyptian-amber">
    <div class="brand-band">Toravelle Works</div>
    <div class="foil-panel">
      <div class="foil-texture" role="img" aria-label="Textured metallic foil in gold and olive tones"></div>
      <span class="fragrance-name">Egyptian Amber</span>
    </div>
    <div class="origin-mark" role="img" aria-label="Small outline of Australia"></div>
  </section>
  <section class="box-front coconut-lime">
    <div class="brand-band">Toravelle Works</div>
    <div class="foil-panel">
      <div class="foil-texture" role="img" aria-label="Textured metallic foil in lime green tones"></div>
      <span class="fragrance-name">Coconut Lime</span>
    </div>
    <div class="origin-mark" role="img" aria-label="Small outline of Australia"></div>
  </section>
  <section class="box-front cotton-candy">
    <div class="brand-band">Toravelle Works</div>
    <div class="foil-panel">
      <div class="foil-texture" role="img" aria-label="Textured metallic foil in soft blue tones"></div>
      <span class="fragrance-name">Cotton Candy</span>
    </div>
    <div class="origin-mark" role="img" aria-label="Small outline of Australia"></div>
  </section>
  <section class="box-front cherry-blossom">
    <div class="brand-band">Toravelle Works</div>
    <div class="foil-panel">
      <div class="foil-texture" role="img" aria-label="Textured metallic foil in pink and magenta tones"></div>
      <span class="fragrance-name">Cherry Blossom</span>
    </div>
    <div class="origin-mark" role="img" aria-label="Small outline of Australia"></div>
  </section>
</main>
</body>
</html>
```